Catalog Design for herbal supplement products

We need a product catalog for several of our new dietary supplement products. We specialize in herbal formula, so we want our catalog to have some pictures of herbs, greens, flowers, plants for nature's feeling. We would like to see the catalog matches the color of our logo ( attached file). We need a text area with clear, readable fond and size for product description.

P.S.: I just upload another file called "catalog sample", please go and checkout this picture and see what kind of feeling I'm looking for. Please DO NOT just copy the catalog design from this sample. I'm just giving you a feeling of the catalog I want.

Requirements
Must have
• one page must display 2~3 products, with bottles pics, supplement fact table, text area for description.
• professional looking, neat and clean displays
• easy to read fond, size text
• good layout between bottles pics, supplement fact tables, texts and herbal images
Nice to have
• high quality, copyright-free herbs, greens, flowers, plants images associated with co-related products to decorate the catalog
Should not have
• must NOT be overly messy and hard-to-read

```html
<!DOCTYPE html>
<html lang="en">
<head>
<meta charset="utf-8">
<title>Leafwell Herbal Catalog 2017 – Pages 12–13</title>
<link href="https://fonts.googleapis.com/css2?family=Titillium+Web:wght@400;600;700&family=Open+Sans:wght@400;600;700&display=swap" rel="stylesheet">
<style>
  :root{
    --leaf:#8cb83a;
    --leaf-dark:#6e9a23;
    --ink:#2b2b2b;
    --muted:#6d6d6d;
    --rule:#444;
    --paper:#ffffff;
    --backdrop:#e4e3df;
    --bottle-top:#2f6b3c;
    --bottle-bottom:#173d22;
  }
  *{box-sizing:border-box;margin:0;padding:0}
  html,body{width:1200px;height:804px;overflow:hidden}
  body{background:var(--backdrop);font-family:"Open Sans",sans-serif;color:var(--ink)}
  .spread{position:absolute;left:30px;top:22px;width:1140px;height:760px;display:flex;box-shadow:0 4px 18px rgba(0,0,0,.15)}
  .page{position:relative;width:570px;height:760px;background:var(--paper)}
  .page--left{border-right:1px solid #ddd}
  .web-band{position:absolute;top:30px;height:22px;width:210px;background:var(--leaf);color:#fff;font-size:9px;letter-spacing:2px;display:flex;align-items:center;gap:8px;padding:0 16px}
  .page--left .web-band{left:0;clip-path:polygon(0 0,100% 0,92% 100%,0 100%)}
  .page--right .web-band{right:0;justify-content:flex-end;clip-path:polygon(0 0,100% 0,100% 100%,8% 100%)}
  .web-band svg{width:11px;height:11px}
  .brand{position:absolute;top:30px;display:flex;align-items:center;gap:6px;font-family:"Titillium Web",sans-serif;font-weight:600;font-size:18px;color:var(--leaf-dark)}
  .page--left .brand{right:40px}
  .page--right .brand{left:40px}
  .brand-dot{width:10px;height:10px;border-radius:50%;background:var(--leaf)}
  .products{position:absolute;top:70px;left:0;right:0}
  .product{display:flex;align-items:flex-start;gap:28px;height:200px;margin-bottom:10px;padding:0 36px}
  .page--right .product{flex-direction:row-reverse}
  .product-frame{flex:0 0 190px;height:168px;border:2px solid var(--leaf);border-radius:12px;display:flex;align-items:center;justify-content:center;margin-top:6px}
  .bottle-photo{width:68px;height:120px;border-radius:12px 12px 8px 8px;background:linear-gradient(180deg,var(--bottle-top),var(--bottle-bottom))}
  .product-info{flex:1}
  .product-title{font-family:"Titillium Web",sans-serif;font-weight:700;font-size:21px;line-height:1;color:var(--ink);text-transform:uppercase}
  .product-title .accent{color:var(--leaf)}
  .product-desc{font-size:8.5px;line-height:1.5;color:var(--muted);margin:4px 0 5px}
  .facts{width:100%;border:1px solid var(--rule);padding:3px 6px;font-size:6px;line-height:1.25}
  .facts-head{font-weight:700;font-size:7.5px}
  .facts-meta{color:var(--muted);border-bottom:3px solid var(--rule);padding-bottom:2px}
  .facts table{width:100%;border-collapse:collapse}
  .facts th{text-align:right;font-weight:600;border-bottom:1px solid var(--rule);padding:1px 0 1px 6px;white-space:nowrap}
  .facts td{border-bottom:1px solid #999;padding:1px 0;vertical-align:top}
  .facts td.num{text-align:right;white-space:nowrap;padding-left:6px}
  .facts td strong{font-weight:700}
  .facts .note{color:var(--muted);padding-top:1px}
  .other{font-size:5.8px;line-height:1.3;color:var(--muted);margin-top:2px}
  .contact{position:absolute;bottom:42px;font-size:9px;color:var(--muted);font-weight:600}
  .page--left .contact{right:36px}
  .page--right .contact{left:36px}
  .contact span{color:var(--leaf-dark)}
  .folio{position:absolute;bottom:20px;font-size:9px;color:var(--muted)}
  .folio b{color:var(--leaf-dark)}
  .page--left .folio{left:36px}
  .page--right .folio{right:36px}
</style>
</head>
<body>
<main class="spread">

  <section class="page page--left">
    <div class="web-band"><svg viewBox="0 0 12 12"><circle cx="6" cy="6" r="6" fill="#fff"/><path d="M3 6h5M6 3.5 8.5 6 6 8.5" stroke="#8cb83a" stroke-width="1.4" fill="none"/></svg>www.leafwellherbs.com</div>
    <div class="brand"><span class="brand-dot"></span>Leafwell</div>
    <div class="products">
      <article class="product">
        <div class="product-frame"><div class="bottle-photo" role="img" aria-label="Green supplement bottle of Clear Mind capsules"></div></div>
        <div class="product-info">
          <h2 class="product-title"><span class="accent">Clear</span> Mind</h2>
          <p class="product-desc">Ginkgo Biloba Complex Capsules – Ginkgo Biloba, Cistanche Tubulosa, Turmeric Extract, Fo-ti Extract Combination</p>
          <div class="facts">
            <div class="facts-head">Supplement Facts</div>
            <div class="facts-meta">Serving Size: 2 Veggie Capsules<br>Servings per Container: 30</div>
            <table>
              <tr><th></th><th>Amount Per Serving</th><th>% Daily Value</th></tr>
              <tr><td><strong>Bitter Melon 10:1 Extract</strong></td><td class="num">500 mg</td><td class="num">*</td></tr>
              <tr><td><strong>Pomegranate Extract</strong> (Standardized to 40% Ellagic Acid)</td><td class="num">500 mg</td><td class="num">*</td></tr>
              <tr><td><strong>Cinnamon 10:1 Extract</strong> Cinnamomum cassia (Bark)</td><td class="num">300 mg</td><td class="num">*</td></tr>
              <tr><td><strong>Astragalus (root)</strong></td><td class="num">60 mg</td><td class="num">*</td></tr>
              <tr><td><strong>Vegetarian Blend</strong> Asparagus, Brussel Sprout, Cabbage, Carrot, Cauliflower, Celery, Cucumber, Green Bell Pepper, Beet, Kale, Parsley, Spinach, Tomato, Wheat Grass</td><td class="num">100 mg</td><td class="num">*</td></tr>
            </table>
            <div class="note">*Daily value not established.</div>
          </div>
          <p class="other">Other ingredients: vegetarian capsules.</p>
        </div>
      </article>
      <article class="product">
        <div class="product-frame"><div class="bottle-photo" role="img" aria-label="Green supplement bottle of Clear Mind capsules"></div></div>
        <div class="product-info">
          <h2 class="product-title"><span class="accent">Clear</span> Mind</h2>
          <p class="product-desc">Ginkgo Biloba Complex Capsules – Ginkgo Biloba, Cistanche Tubulosa, Turmeric Extract, Fo-ti Extract Combination</p>
          <div class="facts">
            <div class="facts-head">Supplement Facts</div>
            <div class="facts-meta">Serving Size: 2 Veggie Capsules<br>Servings per Container: 30</div>
            <table>
              <tr><th></th><th>Amount Per Serving</th><th>% Daily Value</th></tr>
              <tr><td><strong>Bitter Melon 10:1 Extract</strong></td><td class="num">500 mg</td><td class="num">*</td></tr>
              <tr><td><strong>Pomegranate Extract</strong> (Standardized to 40% Ellagic Acid)</td><td class="num">500 mg</td><td class="num">*</td></tr>
              <tr><td><strong>Cinnamon 10:1 Extract</strong> Cinnamomum cassia (Bark)</td><td class="num">300 mg</td><td class="num">*</td></tr>
              <tr><td><strong>Astragalus (root)</strong></td><td class="num">60 mg</td><td class="num">*</td></tr>
              <tr><td><strong>Vegetarian Blend</strong> Asparagus, Brussel Sprout, Cabbage, Carrot, Cauliflower, Celery, Cucumber, Green Bell Pepper, Beet, Kale, Parsley, Spinach, Tomato, Wheat Grass</td><td class="num">100 mg</td><td class="num">*</td></tr>
            </table>
            <div class="note">*Daily value not established.</div>
          </div>
          <p class="other">Other ingredients: vegetarian capsules.</p>
        </div>
      </article>
      <article class="product">
        <div class="product-frame"><div class="bottle-photo" role="img" aria-label="Green supplement bottle of Clear Mind capsules"></div></div>
        <div class="product-info">
          <h2 class="product-title"><span class="accent">Clear</span> Mind</h2>
          <p class="product-desc">Ginkgo Biloba Complex Capsules – Ginkgo Biloba, Cistanche Tubulosa, Turmeric Extract, Fo-ti Extract Combination</p>
          <div class="facts">
            <div class="facts-head">Supplement Facts</div>
            <div class="facts-meta">Serving Size: 2 Veggie Capsules<br>Servings per Container: 30</div>
            <table>
              <tr><th></th><th>Amount Per Serving</th><th>% Daily Value</th></tr>
              <tr><td><strong>Bitter Melon 10:1 Extract</strong></td><td class="num">500 mg</td><td class="num">*</td></tr>
              <tr><td><strong>Pomegranate Extract</strong> (Standardized to 40% Ellagic Acid)</td><td class="num">500 mg</td><td class="num">*</td></tr>
              <tr><td><strong>Cinnamon 10:1 Extract</strong> Cinnamomum cassia (Bark)</td><td class="num">300 mg</td><td class="num">*</td></tr>
              <tr><td><strong>Astragalus (root)</strong></td><td class="num">60 mg</td><td class="num">*</td></tr>
              <tr><td><strong>Vegetarian Blend</strong> Asparagus, Brussel Sprout, Cabbage, Carrot, Cauliflower, Celery, Cucumber, Green Bell Pepper, Beet, Kale, Parsley, Spinach, Tomato, Wheat Grass</td><td class="num">100 mg</td><td class="num">*</td></tr>
            </table>
            <div class="note">*Daily value not established.</div>
          </div>
          <p class="other">Other ingredients: vegetarian capsules.</p>
        </div>
      </article>
    </div>
    <p class="contact">Phone: 555-210-4480 | <span>hello@leafwellherbs.com</span></p>
    <p class="folio"><b>PAGE 12</b> | Herbal Catalog 2017</p>
  </section>

  <section class="page page--right">
    <div class="web-band">www.leafwellherbs.com<svg viewBox="0 0 12 12"><circle cx="6" cy="6" r="6" fill="#fff"/><path d="M9 6H4M6 3.5 3.5 6 6 8.5" stroke="#8cb83a" stroke-width="1.4" fill="none"/></svg></div>
    <div class="brand"><span class="brand-dot"></span>Leafwell</div>
    <div class="products">
      <article class="product">
        <div class="product-frame"><div class="bottle-photo" role="img" aria-label="Green supplement bottle of Clear Mind capsules"></div></div>
        <div class="product-info">
          <h2 class="product-title"><span class="accent">Clear</span> Mind</h2>
          <p class="product-desc">Ginkgo Biloba Complex Capsules – Ginkgo Biloba, Cistanche Tubulosa, Turmeric Extract, Fo-ti Extract Combination</p>
          <div class="facts">
            <div class="facts-head">Supplement Facts</div>
            <div class="facts-meta">Serving Size: 2 Veggie Capsules<br>Servings per Container: 30</div>
            <table>
              <tr><th></th><th>Amount Per Serving</th><th>% Daily Value</th></tr>
              <tr><td><strong>Bitter Melon 10:1 Extract</strong></td><td class="num">500 mg</td><td class="num">*</td></tr>
              <tr><td><strong>Pomegranate Extract</strong> (Standardized to 40% Ellagic Acid)</td><td class="num">500 mg</td><td class="num">*</td></tr>
              <tr><td><strong>Cinnamon 10:1 Extract</strong> Cinnamomum cassia (Bark)</td><td class="num">300 mg</td><td class="num">*</td></tr>
              <tr><td><strong>Astragalus (root)</strong></td><td class="num">60 mg</td><td class="num">*</td></tr>
              <tr><td><strong>Vegetarian Blend</strong> Asparagus, Brussel Sprout, Cabbage, Carrot, Cauliflower, Celery, Cucumber, Green Bell Pepper, Beet, Kale, Parsley, Spinach, Tomato, Wheat Grass</td><td class="num">100 mg</td><td class="num">*</td></tr>
            </table>
            <div class="note">*Daily value not established.</div>
          </div>
          <p class="other">Other ingredients: vegetarian capsules.</p>
        </div>
      </article>
      <article class="product">
        <div class="product-frame"><div class="bottle-photo" role="img" aria-label="Green supplement bottle of Clear Mind capsules"></div></div>
        <div class="product-info">
          <h2 class="product-title"><span class="accent">Clear</span> Mind</h2>
          <p class="product-desc">Ginkgo Biloba Complex Capsules – Ginkgo Biloba, Cistanche Tubulosa, Turmeric Extract, Fo-ti Extract Combination</p>
          <div class="facts">
            <div class="facts-head">Supplement Facts</div>
            <div class="facts-meta">Serving Size: 2 Veggie Capsules<br>Servings per Container: 30</div>
            <table>
              <tr><th></th><th>Amount Per Serving</th><th>% Daily Value</th></tr>
              <tr><td><strong>Bitter Melon 10:1 Extract</strong></td><td class="num">500 mg</td><td class="num">*</td></tr>
              <tr><td><strong>Pomegranate Extract</strong> (Standardized to 40% Ellagic Acid)</td><td class="num">500 mg</td><td class="num">*</td></tr>
              <tr><td><strong>Cinnamon 10:1 Extract</strong> Cinnamomum cassia (Bark)</td><td class="num">300 mg</td><td class="num">*</td></tr>
              <tr><td><strong>Astragalus (root)</strong></td><td class="num">60 mg</td><td class="num">*</td></tr>
              <tr><td><strong>Vegetarian Blend</strong> Asparagus, Brussel Sprout, Cabbage, Carrot, Cauliflower, Celery, Cucumber, Green Bell Pepper, Beet, Kale, Parsley, Spinach, Tomato, Wheat Grass</td><td class="num">100 mg</td><td class="num">*</td></tr>
            </table>
            <div class="note">*Daily value not established.</div>
          </div>
          <p class="other">Other ingredients: vegetarian capsules.</p>
        </div>
      </article>
      <article class="product">
        <div class="product-frame"><div class="bottle-photo" role="img" aria-label="Green supplement bottle of Clear Mind capsules"></div></div>
        <div class="product-info">
          <h2 class="product-title"><span class="accent">Clear</span> Mind</h2>
          <p class="product-desc">Ginkgo Biloba Complex Capsules – Ginkgo Biloba, Cistanche Tubulosa, Turmeric Extract, Fo-ti Extract Combination</p>
          <div class="facts">
            <div class="facts-head">Supplement Facts</div>
            <div class="facts-meta">Serving Size: 2 Veggie Capsules<br>Servings per Container: 30</div>
            <table>
              <tr><th></th><th>Amount Per Serving</th><th>% Daily Value</th></tr>
              <tr><td><strong>Bitter Melon 10:1 Extract</strong></td><td class="num">500 mg</td><td class="num">*</td></tr>
              <tr><td><strong>Pomegranate Extract</strong> (Standardized to 40% Ellagic Acid)</td><td class="num">500 mg</td><td class="num">*</td></tr>
              <tr><td><strong>Cinnamon 10:1 Extract</strong> Cinnamomum cassia (Bark)</td><td class="num">300 mg</td><td class="num">*</td></tr>
              <tr><td><strong>Astragalus (root)</strong></td><td class="num">60 mg</td><td class="num">*</td></tr>
              <tr><td><strong>Vegetarian Blend</strong> Asparagus, Brussel Sprout, Cabbage, Carrot, Cauliflower, Celery, Cucumber, Green Bell Pepper, Beet, Kale, Parsley, Spinach, Tomato, Wheat Grass</td><td class="num">100 mg</td><td class="num">*</td></tr>
            </table>
            <div class="note">*Daily value not established.</div>
          </div>
          <p class="other">Other ingredients: vegetarian capsules.</p>
        </div>
      </article>
    </div>
    <p class="contact">Phone: 555-210-4480 | <span>hello@leafwellherbs.com</span></p>
    <p class="folio">Herbal Catalog 2017 | <b>PAGE 13</b></p>
  </section>

</main>
</body>
</html>
```